Business Brochure Design Project

BRIGHTWATER FIELD SERVICES
Our company requires a business brochure designed, this design will be printed and emailed to prospective corporate clients to provide an understanding of our businesses services. The written content required in this brochure is attached as a word document.

DESIGN
The design needs to hold your attention and identify the company brand. An A4 portrait format will be used with a white background. Brochure pages will never be viewed side by side as most clients will recieve this as a pdf document attached to an email so considered this in your design. Colour graphics and images will be used to enhance the content and draw people in. To reflect quality, only high resolution images that are clear, sharp and in focus will be used. Please use the CMYK colour model when designing as this brochure will also be printed.

LOOK AND FEEL
The design needs to be savvy, appear uncluttered and have an attitude of a market leader. I want something that stands out in the crowd and effectively markets my businesses brand. It needs to be elegant, modern and have a corporate feel. I want something that has energy, is fresh, innovative, exciting and inviting.

FINISHED PRODUCT
All content in the photo shop design needs to be fully editable including text. Our business has a copy of photo shop CS6, so the finished product must be compatible with this version of software. Each page must contain the text “Copyright © 2013 Brightwater Field Services. All rights reserved”
Updates

Hi all

I will also be setting up a stationay project soon, if your are interested in being part of it please let me know.

Thanks

                          

I like designs that use a white background with the use of red, black and grey colours within

 

To all designers

Thanks for the great design work; I look forward to working with you all again in the future

 

Regards Marcus Henley

Industry/Entity Type

Shop

Requirements
Must have
• This design must be professional and of the highest calibre

Please use the CMYK colour model as this is the formatt by printers.

Business contact details must be clearly visible on the cover page
Should not have
• Each part of my business advertising needs to look interesting in its own right. This insures companies are intrigued to find out more about our services, who we are and what we do. Please do not design something that looks identical to my webpage site or Facebook page. Your design needs to adds value to the overall promotional impact of my business.

The design should not be based off a generic design template, it needs to be unique.

```html
<!DOCTYPE html>
<html lang="en">
<head>
<meta charset="utf-8">
<title>Brightwater Field Services – Testimonials</title>
<link rel="stylesheet" href="https://fonts.googleapis.com/css2?family=Arimo:ital,wght@1,400&family=Roboto+Condensed:wght@700&display=swap">
<style>
  :root {
    --ink: #1e1b1c;
    --paper: #ffffff;
    --text: #222222;
    --photo-light: #d9d6cf;
    --photo-mid: #a9a49a;
    --photo-dark: #5a5650;
  }
  html, body {
    margin: 0;
    padding: 0;
    overflow: hidden;
    background: var(--paper);
  }
  .page {
    position: relative;
    width: 1200px;
    height: 1000px;
    overflow: hidden;
    background: var(--paper);
  }
  .brand-band {
    position: absolute;
    left: 0;
    top: 0;
  }
  .brand-name {
    position: absolute;
    left: 34px;
    top: 48px;
    margin: 0;
    font-family: "Roboto Condensed", "Arial Narrow", sans-serif;
    font-weight: 700;
    font-size: 24px;
    line-height: 1.15;
    letter-spacing: 1px;
    color: var(--paper);
  }
  .page-title {
    position: absolute;
    right: 63px;
    top: 98px;
    margin: 0;
    font-family: "Roboto Condensed", "Arial Narrow", sans-serif;
    font-weight: 700;
    font-size: 42px;
    line-height: 1;
    color: var(--ink);
    transform: scaleX(0.92);
    transform-origin: right;
  }
  .portraits {
    position: absolute;
    left: 0;
    top: 0;
  }
  .testimonial {
    position: absolute;
    left: 363px;
    width: 800px;
    margin: 0;
  }
  .testimonial-quote {
    margin: 0;
    font-family: "Arimo", Arial, sans-serif;
    font-style: italic;
    font-size: 21.4px;
    line-height: 27.5px;
    color: var(--text);
    white-space: nowrap;
  }
  .testimonial-credit {
    position: absolute;
    right: 18px;
    margin: 0;
    width: 435px;
    padding-bottom: 8px;
    border-bottom: 2px solid var(--ink);
    text-align: right;
    font-family: "Arimo", Arial, sans-serif;
    font-style: italic;
    font-size: 16px;
    color: var(--text);
    word-spacing: 14px;
  }
  .credit-inner { padding-right: 22px; }
</style>
</head>
<body>
<main class="page">
  <svg class="brand-band" width="660" height="220" viewBox="0 0 660 220" aria-hidden="true">
    <path d="M0 0 H640 C420 70 180 120 0 212 Z" fill="var(--ink)"/>
  </svg>
  <p class="brand-name">BRIGHTWATER<br>FIELD SERVICES</p>

  <h1 class="page-title">TESTIMONIALS</h1>

  <svg class="portraits" width="340" height="1000" viewBox="0 0 340 1000">
    <defs>
      <linearGradient id="portrait-tone" x1="0" y1="0" x2="1" y2="1">
        <stop offset="0" stop-color="var(--photo-light)"/>
        <stop offset="0.55" stop-color="var(--photo-mid)"/>
        <stop offset="1" stop-color="var(--photo-dark)"/>
      </linearGradient>
    </defs>
    <path role="img" aria-label="Portrait photo of a smiling client in a business suit"
          d="M0 262 L334 183 L292 540 C200 560 90 600 0 645 Z" fill="url(#portrait-tone)"/>
    <path role="img" aria-label="Portrait photo of a smiling businessman"
          d="M0 690 C110 630 230 580 334 548 L290 905 C190 925 80 950 0 985 Z" fill="url(#portrait-tone)"/>
    <path role="img" aria-label="Portrait photo of a third client"
          d="M0 1000 L0 1000 C110 960 230 925 334 905 L325 1000 Z" fill="url(#portrait-tone)"/>
  </svg>

  <section class="testimonial" style="top:210px">
    <p class="testimonial-quote">I had the opportunity to work with Marcus within the Coral Ridge LNG project in<br>Queensland. He was a pleasure to work with and had skills that in my<br>experience few people possess. He was assertive, proactive and applied<br>himself and his experience to ensure cost and project controls were clear and<br>reporting was on time. He worked very well within the team environment and<br>was always willing to get involved and help in many ways others couldn't.<br>His varied experiences with in the Mining, Oil and Gas industries would be a<br>definite asset to any company looking for an industry provider to provide on<br>time cost and controls schedules.&nbsp; I would definitely recommend him and look<br>forward to working with him again.</p>
    <p class="testimonial-credit" style="top:294px"><span class="credit-inner">NAME TITLE PROJECT</span></p>
  </section>

  <section class="testimonial" style="top:567px">
    <p class="testimonial-quote">I had the opportunity to work with Marcus within the Coral Ridge LNG project in<br>Queensland. He was a pleasure to work with and had skills that in my<br>experience few people possess. He was assertive, proactive and applied<br>himself and his experience to ensure cost and project controls were clear and<br>reporting was on time. He worked very well within the team environment and<br>was always willing to get involved and help in many ways others couldn't.<br>His varied experiences with in the Mining, Oil and Gas industries would be a<br>definite asset to any company looking for an industry provider to provide on<br>time cost and controls schedules.&nbsp; I would definitely recommend him and look<br>forward to working with him again.</p>
    <p class="testimonial-credit" style="top:287px"><span class="credit-inner">NAME TITLE PROJECT</span></p>
  </section>

  <section class="testimonial" style="top:925px">
    <p class="testimonial-quote">I had the opportunity to work with Marcus within the Coral Ridge LNG project in<br>Queensland. He was a pleasure to work with and had skills that in my<br>experience few people possess. He was assertive, proactive and applied</p>
  </section>
</main>
</body>
</html>
```